11 x 11 Flyer Design for Social Media - Reverse Mortgages

62 or older?

A Reverse Mortgage
could be
Your Road to Financial Freedom

* No Monthly Payments
* No Income Requirements
* No Credit Score Requirements
* No Loss of Ownership

Receive cash by lump sum, monthly installments or a line of credit!!

Call us today for a Free Consultation!!
(800) 471-2965

Bluegate Financial Services, Inc.
NMLS #318760
www.bluegatehome.com

```html
<!DOCTYPE html>
<html lang="en">
<head>
<meta charset="utf-8">
<title>Reverse Mortgage Flyer</title>
<link rel="stylesheet" href="https://fonts.googleapis.com/css2?family=Open+Sans:wght@800&family=Open+Sans+Condensed:wght@700&family=Raleway:wght@400;500;700&display=swap">
<style>
:root{
  --blue:#2a5aa0;
  --blue-deep:#1b3f78;
  --olive:#9a9a1e;
  --olive-dark:#7d7a0c;
  --cream:#e9e6cc;
  --ink:#141414;
  --white:#ffffff;
}
*{margin:0;padding:0;box-sizing:border-box}
html,body{width:1200px;height:1200px;overflow:hidden;background:var(--white)}
.flyer{position:relative;width:1200px;height:1200px;overflow:hidden;background:var(--white);font-family:"Raleway",sans-serif;color:var(--ink)}
.art{position:absolute;inset:0;width:1200px;height:1200px}
.headline{position:absolute;left:50px;top:56px;font-family:"Open Sans",sans-serif;font-weight:800;font-size:82px;line-height:1;color:var(--blue);letter-spacing:1px}
.subhead{position:absolute;left:50px;top:170px;font-weight:500;font-size:36px;line-height:47px;text-transform:uppercase}
.freedom{position:absolute;left:48px;top:302px;font-family:"Open Sans",sans-serif;font-weight:800;font-size:100px;line-height:1;color:var(--olive)}
.benefits{position:absolute;left:60px;top:604px;list-style:none}
.benefits li{display:flex;align-items:center;height:48px;font-size:36px;font-weight:400}
.benefits svg{width:24px;height:24px;margin-right:26px;flex:none}
.payout{position:absolute;left:54px;top:816px;font-weight:700;font-size:33px;line-height:43px;color:var(--olive)}
.cta{position:absolute;left:54px;top:944px;width:662px;height:78px;border-radius:0 24px 24px 0;background:linear-gradient(90deg,var(--olive-dark),#9c9a14 55%,#8a8610);display:flex;align-items:center;padding-left:35px;font-family:"Open Sans Condensed",sans-serif;font-weight:700;font-size:40px;color:#f4f1d6;box-shadow:-6px 4px 6px rgba(0,0,0,.35)}
.contact{position:absolute;left:58px;top:1052px;list-style:none;color:var(--white);font-family:Arial,sans-serif;font-size:22px}
.contact li{display:flex;align-items:center;height:38px}
.contact svg{width:22px;height:22px;margin-right:24px;flex:none}
.brand{position:absolute;left:830px;top:1020px;width:300px;display:flex;align-items:center;gap:12px;font-weight:700;font-size:20px;line-height:24px;color:var(--blue)}
.brand-dot{width:34px;height:34px;border-radius:50%;background:var(--blue);flex:none}
</style>
</head>
<body>
<main class="flyer">
  <svg class="art" viewBox="0 0 1200 1200" aria-hidden="false">
    <defs>
      <linearGradient id="heroTone" x1="0" y1="0" x2="1" y2="0">
        <stop offset="0" stop-color="#ffffff"/>
        <stop offset=".4" stop-color="#e9eef2"/>
        <stop offset=".7" stop-color="#b9c7d3"/>
        <stop offset="1" stop-color="#c8d2db"/>
      </linearGradient>
      <linearGradient id="carTone" x1="0" y1="0" x2="1" y2="1">
        <stop offset="0" stop-color="#d7d2c3"/>
        <stop offset=".5" stop-color="#8a7464"/>
        <stop offset="1" stop-color="#5a6f9a"/>
      </linearGradient>
      <linearGradient id="bandBlue" x1="0" y1="0" x2="1" y2="0">
        <stop offset="0" stop-color="#2a5aa0"/>
        <stop offset="1" stop-color="#1b3f78"/>
      </linearGradient>
    </defs>

    <rect class="hero-photo" x="0" y="0" width="1200" height="600" fill="url(#heroTone)" role="img" aria-label="Photo of a smiling senior couple in white on a beach"/>

    <!-- upper sweep -->
    <path d="M0 520 Q420 380 760 450 L760 470 Q420 410 0 540 Z" fill="var(--olive)"/>
    <path d="M0 540 Q420 410 760 470 L800 520 Q360 440 0 660 Z" fill="url(#bandBlue)"/>
    <path d="M0 560 Q420 430 780 490" fill="none" stroke="#fff" stroke-width="2"/>
    <path d="M0 660 Q360 440 800 520 L800 1200 L0 1200 Z" fill="#fff"/>
    <path d="M310 536 Q620 540 860 640 L900 760 Q700 600 430 540 Z" fill="var(--cream)"/>
    <path d="M1000 870 L1200 930 L1200 1030 Z" fill="var(--cream)"/>

    <!-- lower sweep -->
    <path d="M0 1000 Q300 930 700 990 Q880 1060 940 1140 Q1080 1160 1200 1100 L1200 1200 L0 1200 Z" fill="var(--olive)"/>
    <path d="M0 1020 Q300 955 690 1010 Q860 1080 920 1150 Q1080 1180 1200 1110 L1200 1200 L0 1200 Z" fill="url(#bandBlue)"/>
    <ellipse cx="970" cy="1060" rx="245" ry="112" fill="#fff"/>

    <!-- circle photo -->
    <circle cx="945" cy="628" r="291" fill="none" stroke="var(--olive)" stroke-width="2.5" stroke-dasharray="2 5"/>
    <circle cx="945" cy="628" r="262" fill="#fff"/>
    <circle class="car-photo" cx="945" cy="628" r="252" fill="url(#carTone)" role="img" aria-label="Photo of a laughing senior couple riding in a convertible"/>
    <circle cx="945" cy="628" r="257" fill="none" stroke="var(--blue)" stroke-width="10"/>
  </svg>

  <h1 class="headline">62 OR OLDER?</h1>
  <p class="subhead">A Reverse Mortgage<br>could be your<br>road to financial</p>
  <p class="freedom">FREEDOM</p>

  <ul class="benefits">
    <li><svg viewBox="0 0 24 24"><circle cx="12" cy="12" r="10" fill="none" stroke="#9a9a1e" stroke-width="2" stroke-dasharray="50 13"/><path d="M7 12l4 4 8-9" fill="none" stroke="#9a9a1e" stroke-width="2.4"/></svg>No Monthly Payments</li>
    <li><svg viewBox="0 0 24 24"><circle cx="12" cy="12" r="10" fill="none" stroke="#9a9a1e" stroke-width="2" stroke-dasharray="50 13"/><path d="M7 12l4 4 8-9" fill="none" stroke="#9a9a1e" stroke-width="2.4"/></svg>No Income Requirements</li>
    <li><svg viewBox="0 0 24 24"><circle cx="12" cy="12" r="10" fill="none" stroke="#9a9a1e" stroke-width="2" stroke-dasharray="50 13"/><path d="M7 12l4 4 8-9" fill="none" stroke="#9a9a1e" stroke-width="2.4"/></svg>No Credit Score Requirements</li>
    <li><svg viewBox="0 0 24 24"><circle cx="12" cy="12" r="10" fill="none" stroke="#9a9a1e" stroke-width="2" stroke-dasharray="50 13"/><path d="M7 12l4 4 8-9" fill="none" stroke="#9a9a1e" stroke-width="2.4"/></svg>No Loss of Ownership</li>
  </ul>

  <p class="payout">Receive cash by lump sum, monthly<br>installments or a line of credit!!</p>

  <div class="cta">Call us today for a Free Consultation!!</div>

  <ul class="contact">
    <li><svg viewBox="0 0 24 24"><path d="M6 3l3 5-2 2c1 3 4 6 7 7l2-2 5 3-2 4C11 22 2 13 3 5z" fill="#f2d21b"/></svg>(800) 471-2965</li>
    <li><svg viewBox="0 0 24 24"><circle cx="12" cy="12" r="10" fill="#f2d21b"/><path d="M7 6c3 1 2 4 5 5s1 5 3 7M14 4c1 2 4 3 6 3" fill="none" stroke="#1b3f78" stroke-width="2"/></svg>www.bluegatehome.com</li>
    <li><svg viewBox="0 0 24 24"><path d="M12 2a7 7 0 0 0-7 7c0 5 7 13 7 13s7-8 7-13a7 7 0 0 0-7-7zm0 4a3 3 0 1 1 0 6 3 3 0 0 1 0-6z" fill="#f2d21b"/></svg>Bluegate Financial Services, Inc. NMLS #318760</li>
  </ul>

  <div class="brand"><span class="brand-dot"></span><span>Bluegate Financial Services, Inc.</span></div>
</main>
</body>
</html>
```